QERO brochure

I need a Double gatefold brochure (quad fold) designed for our medical group. I've attached some sample content and where it should all appear on the brochure. At this point, I'm looking for a general mock-up of the content to see how it will fit and look. After I find an acceptable design, I will be able to provide all the pictures, etc. I also understand that the amount of written content may be too much to look good on the brochure and can edit as deemed necessary and the content may be somewhat redundant-just looking for the general layout first and then I'll edit content. Thanks. Looking forward to seeing your designs!

Target Market(s)

This is a brochure that will given to patients to help identify who their doctor will be while they are in the hospital. It will also help to explain who we are and why their primary care doctor isn't seeing them in the hospital

Industry/Entity Type

Medical

Font styles to use
Sans Serif

Colors
0355a3
3176b5
85acd3

Requirements
Must have
• interior pictures in a quad-fold double gatefold format. Pictures need to have boxes in the lower L hand corner so that we can "check" who the doctor is that is assigned to the patient. Also having the lines to hand write the attending, resident and intern is necessary
Nice to have
• As much written content as possible but I want to look at the amount so that I can make sure that the brochure is visually appealing. All of our current products use Helvetica font so consistency would be nice
Should not have
• Needs to be modern and professional. Not too playful or casual-we are a professional group working in a hospital setting with very sick patients.

```html
<!DOCTYPE html>
<html lang="en">
<head>
<meta charset="utf-8">
<title>QERO brochure</title>
<link href="https://fonts.googleapis.com/css2?family=Open+Sans:ital,wght@0,400;0,600;0,700;1,400;1,600&display=swap" rel="stylesheet">
<style>
  :root {
    --blue-deep: #0355a3;
    --blue-mid: #3176b5;
    --blue-soft: #85acd3;
    --blue-dark: #02407d;
    --paper: #f3f4f6;
    --canvas: #d9dadc;
    --white: #ffffff;
    --ink: #2a2f38;
  }
  * { box-sizing: border-box; margin: 0; padding: 0; }
  html, body { width: 1200px; height: 800px; overflow: hidden; }
  body {
    background: var(--canvas);
    font-family: "Open Sans", Helvetica, Arial, sans-serif;
    color: var(--white);
  }
  .brochure {
    position: absolute; left: 40px; top: 90px;
    width: 1120px; height: 620px;
    display: flex;
    box-shadow: 0 10px 30px rgba(0,0,0,.25);
  }
  .panel { position: relative; width: 280px; height: 620px; overflow: hidden; }
  .panel p { font-size: 8.6px; line-height: 1.45; text-align: justify; }
  .panel h2 { font-size: 16px; font-weight: 700; margin-bottom: 8px; }

  /* panel 1 */
  .panel--intro {
    background: linear-gradient(180deg, var(--blue-deep), #044a8f);
    padding: 20px 18px;
  }
  .panel--intro p { font-size: 7.9px; line-height: 1.38; }
  .panel--intro h2 { font-size: 15px; margin-bottom: 6px; }
  .panel--intro p + h2 { margin-top: 22px; }
  .panel--intro p + p { margin-top: 9px; }
  .intro__rule { position: absolute; left: 0; right: 0; top: 484px; height: 7px; background: var(--white); }
  .brand-box {
    position: absolute; left: 18px; right: 18px; top: 508px; height: 96px;
    background: var(--blue-mid); border: 1px solid var(--white);
    padding: 10px 14px;
  }
  .brand-name { font-size: 30px; font-weight: 700; letter-spacing: 1px; color: var(--white); line-height: 1; }
  .brand-sub { font-size: 7px; color: var(--white); margin-top: 2px; }
  .brand-tag { font-size: 19px; font-weight: 400; color: var(--white); margin-top: 16px; }

  /* panel 2 */
  .panel--roles { background: var(--paper); color: #1e2a3a; }
  .panel--roles svg.bg { position: absolute; inset: 0; }
  .roles__lead { position: absolute; left: 18px; right: 18px; top: 22px; color: var(--white); }
  .roles__photo {
    position: absolute; left: 40px; top: 130px; width: 200px; height: 150px;
    background: radial-gradient(circle at 50% 40%, #e6e2de, #d6d8dc 70%);
    opacity: .8;
  }
  .roles__list { position: absolute; left: 18px; right: 18px; top: 272px; list-style: none; }
  .role { margin-bottom: 8px; }
  .role__pill {
    display: flex; align-items: center; gap: 6px;
    background: var(--blue-deep); color: var(--white);
    font-size: 10px; font-weight: 700; padding: 3px 10px; border-radius: 10px;
    margin-bottom: 4px;
  }
  .role__check {
    width: 10px; height: 10px; flex: none;
    background: var(--white); border: 1px solid var(--blue-soft);
  }
  .role p { font-size: 7.4px; line-height: 1.35; font-style: italic; font-weight: 600; color: var(--ink); }
  .role__line {
    display: flex; align-items: flex-end; gap: 4px;
    margin-top: 4px; font-size: 7px; font-weight: 600; color: var(--blue-deep);
  }
  .role__line::after {
    content: ""; flex: 1; border-bottom: 1px solid var(--blue-mid); height: 8px;
  }

  /* panel 3 */
  .panel--cover { background: var(--white); }
  .panel--cover svg.bg { position: absolute; inset: 0; }
  .cover__brand { position: absolute; left: 30px; top: 70px; color: var(--blue-dark); }
  .cover__brand .brand-name { color: #1f2530; font-size: 38px; }
  .cover__brand .brand-sub { color: #1f2530; font-size: 8px; }
  .cover__photo {
    position: absolute; left: 22px; top: 128px; width: 236px; height: 220px;
    background: linear-gradient(180deg, #e9edf2 0%, #c9d3de 60%, #9fb4c9 100%);
  }
  .cover__contact {
    position: absolute; left: 0; right: 0; top: 420px;
    text-align: center; font-family: Arial, Helvetica, sans-serif;
  }
  .address { font-size: 13px; line-height: 1.45; letter-spacing: .5px; }
  .phone { font-size: 16px; font-weight: 700; margin-top: 26px; }
  .email { font-size: 10.5px; margin-top: 6px; }

  /* panel 4 */
  .panel--about { background: var(--blue-deep); padding: 24px 18px; }
  .panel--about .band {
    position: absolute; left: 0; right: 0; height: 7px; background: var(--white);
  }
  .about__partner { position: absolute; left: 18px; right: 18px; top: 22px; }
  .about__text { position: absolute; left: 18px; right: 18px; top: 270px; }
  .about__text p + p { margin-top: 14px; }
</style>
</head>
<body>
<main class="brochure">

  <section class="panel panel--intro">
    <h2>What Is A Hospitalist?</h2>
    <p>Hospitalists are physicians specially trained in caring for patients while they are in the hospital. Our Board Certified Internal Medicine doctors are also specialists in inpatient care and possess extensive expertise in best treatment practices, care coordination and options for post-discharge care. Since Hospitalists are located in the hospital, they can spend more time with their patients, improving care and coordination. Each of our doctors meets with your entire care team daily; this involves other specialist doctors, nurses, case managers, physical/occupational therapists, social workers, pharmacists and others.</p>
    <h2>Coordinated Care:</h2>
    <p>The Quarry Hill Hospitalist Associates Program was designed to help ensure high-quality, coordinated care for patients admitted either through the emergency room or for a stay associated with a surgical procedure. Our team of hospitalists, overseen by a dedicated Medical Director, provides high-touch care oversight for hospital patients and helpful support for primary care physicians and specialists who have limited availability to make rounds. These hospitalists are an integral part of the care team, managing patients' care for their entire stay and coordinating with primary care physicians, specialists, surgeons, nurses and family members to determine the best outcome possible.</p>
    <p>Because the hospitalist sees a patient more than once a day and for longer periods of time, he/she is more attuned to changes occurring during the patient's stay and likely to catch any problems or post-operative complications that might arise. The hospitalist is able to spend time explaining treatments to patients and their family members, ultimately easing anxiety and improving recovery.</p>
    <div class="intro__rule"></div>
    <div class="brand-box">
      <div class="brand-name">QERO</div>
      <div class="brand-sub">Quarry Hill Hospitalist Associates</div>
      <div class="brand-tag">Partnering With You</div>
    </div>
  </section>

  <section class="panel panel--roles">
    <svg class="bg" width="280" height="620" viewBox="0 0 280 620" aria-hidden="true">
      <path d="M0 0 H280 V60 C230 70 150 110 110 200 C90 250 60 280 0 290 Z" fill="var(--blue-deep)"/>
      <path d="M110 200 C150 110 230 70 280 60 V72 C235 84 165 120 124 205 Z" fill="var(--blue-mid)"/>
    </svg>
    <div class="roles__photo" role="img" aria-label="Faded photo of a smiling doctor"></div>
    <p class="roles__lead">During your hospital stay, you may see many different types of doctors. At times, it can be confusing to understand what role each person plays on the healthcare team. In order to clarify some of the confusion, this is the typical role of the various doctors who you may see during your hospital stay:</p>
    <ol class="roles__list">
      <li class="role"><span class="role__pill"><span class="role__check"></span>1. The Attending Physician:</span>
        <p>This is the lead doctor on the team. A fully licensed Internal Medicine specialist, this doctor is a member of the medical staff of the hospital and has completed all schooling, training and licensing requirements to practice medicine. This is the person "in charge" of your care and will communicate with your primary care doctor during your stay.</p>
        <span class="role__line">Name:</span></li>
      <li class="role"><span class="role__pill"><span class="role__check"></span>2. The Resident Physician:</span>
        <p>This doctor has completed his/her medical degree and is now training to be certified in the specialty of Internal Medicine. This doctor is under the supervision of the Attending Physician.</p>
        <span class="role__line">Name:</span></li>
      <li class="role"><span class="role__pill"><span class="role__check"></span>3. The Intern:</span>
        <p>This doctor has completed his/her medical degree and is in their first year of training in their specialty field. This doctor is supervised by the Attending and the Resident Physician.</p>
        <span class="role__line">Name:</span></li>
      <li class="role"><span class="role__pill"><span class="role__check"></span>4. The Medical Student:</span>
        <p>This person is either a 3rd or 4th year student in medical school. They are not yet a doctor, but upon graduating from medical school they will become an Intern. They are supervised by the Attending, the Resident and the Intern on the team.</p></li>
    </ol>
  </section>

  <section class="panel panel--cover">
    <svg class="bg" width="280" height="620" viewBox="0 0 280 620" aria-hidden="true">
      <path d="M0 0 H280 V20 C200 40 120 30 0 60 Z" fill="var(--blue-deep)"/>
      <path d="M0 360 C80 340 170 370 280 330 V620 H0 Z" fill="var(--blue-deep)"/>
      <path d="M0 350 C80 330 170 360 280 318 V332 C170 372 80 342 0 362 Z" fill="var(--blue-mid)"/>
    </svg>
    <div class="cover__brand">
      <div class="brand-name">QERO</div>
      <div class="brand-sub">Quarry Hill Hospitalist Associates</div>
    </div>
    <div class="cover__photo" role="img" aria-label="Group photo of the hospitalist team"></div>
    <div class="cover__contact">
      <div class="address">218 HARLOW STREET, RM. 410<br>LAKEVIEW, CA 90210</div>
      <div class="phone">(555) 014-2290</div>
      <div class="email">E : info@qerohospitalists.com</div>
    </div>
  </section>

  <section class="panel panel--about">
    <div class="about__partner">
      <h2>Partnering With You</h2>
      <p>Hospital care should feel seamless and calm throughout your stay. Our team works closely with your own doctors so nothing is missed. We keep you and your family informed, explain each step clearly and plan a safe return home, offering exceptional care with respect and compassion.</p>
    </div>
    <div class="band" style="top:150px"></div>
    <div class="band" style="top:215px"></div>
    <div class="about__text">
      <h2>About Us :</h2>
      <p>All of our physicians are Board Certified/Eligible in Internal Medicine with a primary focus on Inpatient Hospital Care. We see our patients in the Emergency Department and follow them through the course of their hospital stay including the Intensive Care Unit, the Medical/Surgical units as well as the Acute Rehabilitation Center and Skilled Nursing Unit if necessary. Your physician will coordinate your care throughout your stay from the time you arrive until you are safely discharged back to the care of your primary care provider. If you don't yet have a primary care provider, your hospitalist can assist you in finding one as well.</p>
      <p>Each of our doctors has been hand-picked to be a part of our team based on their exceptional clinical skills, strong sense of integrity and deep commitment to compassionate care. Teamwork is at the heart of our group. Exceptional patient care is the center of our focus.</p>
    </div>
  </section>

</main>
</body>
</html>
```